Business Cards Needed For Veterinary Business

Looking for a business card design for a veterinary blood bank. We would like it to be clean and professional on appearance but still warm and inviting. We would like to utilize our logo and similar coloring. We will use our phone number, email, website, employee name, employee title.

We do not want a bunch of animated animal photos but do not need the style to be as clinical as a laboratory or human medical procedure office.

We are looking for some creative ideas to choose from so that we can generate a standout professional business card for our management team to utilize.

Target Market(s)

professionals

Industry/Entity Type

veterinary

Contact Information for Business Card

employee name, employee title, phone number, website URL, email

Font styles to use
Sans Serif

Colors
0054AA
0677BA
7BADD7
CADEEF
E8F1F8
EB3D1F
EC4F4E
F09395
F8D3D4
FCEDEE

Requirements
Nice to have
• creative design
Should not have
• animated photos

```html
<!DOCTYPE html>
<html lang="en">
<head>
<meta charset="utf-8">
<title>Larkfield Animal Blood Bank – Business Card</title>
<link rel="stylesheet" href="https://fonts.googleapis.com/css2?family=Montserrat:wght@500;600;700;800&display=swap">
<style>
  :root {
    --navy: #0c1b33;
    --navy-deep: #081428;
    --red: #eb2227;
    --blue: #0054aa;
    --white: #ffffff;
    --stage: #dcdee2;
  }
  * { margin: 0; padding: 0; box-sizing: border-box; }
  html, body { width: 1200px; height: 1200px; overflow: hidden; }
  body {
    background: var(--stage);
    font-family: "Montserrat", sans-serif;
    position: relative;
  }
  .card {
    position: absolute;
    left: 170px;
    width: 860px;
    height: 491px;
    border-radius: 40px;
    overflow: hidden;
    box-shadow: 0 10px 30px rgba(0,0,0,0.18);
    border-bottom: 4px solid var(--red);
  }
  .card--front { top: 79px; background: var(--white); }
  .card--back {
    top: 630px;
    background: radial-gradient(ellipse at 55% 45%, #0f2340 0%, var(--navy-deep) 80%);
  }
  .front-band { position: absolute; inset: 0; width: 100%; height: 100%; }

  .brand {
    position: absolute;
    display: flex;
    align-items: center;
    gap: 16px;
  }
  .brand__dot { border-radius: 50%; background: var(--red); flex: none; }
  .brand__name {
    color: var(--red);
    font-weight: 800;
    text-transform: uppercase;
    line-height: 1.05;
    letter-spacing: 0.5px;
  }
  .card--front .brand { left: 150px; top: 80px; }
  .card--front .brand__dot { width: 60px; height: 60px; }
  .card--front .brand__name { font-size: 32px; }
  .card--back .brand { left: 50%; top: 50%; transform: translate(-50%, -50%); gap: 22px; }
  .card--back .brand__dot { width: 90px; height: 90px; }
  .card--back .brand__name { font-size: 46px; }

  .person { position: absolute; left: 70px; top: 372px; }
  .person__name {
    color: var(--red);
    font-weight: 700;
    font-size: 38px;
    letter-spacing: -0.5px;
    line-height: 1;
  }
  .person__title {
    color: var(--white);
    font-weight: 500;
    font-size: 22px;
    margin-top: 6px;
  }

  .contact {
    position: absolute;
    left: 500px;
    top: 258px;
    list-style: none;
  }
  .contact__item {
    display: flex;
    align-items: center;
    gap: 14px;
    color: var(--white);
    font-weight: 500;
    font-size: 20px;
    height: 40px;
  }
  .contact__icon { width: 22px; height: 22px; flex: none; }
</style>
</head>
<body>

<section class="card card--front" aria-label="Business card front">
  <svg class="front-band" viewBox="0 0 860 491" preserveAspectRatio="none" aria-hidden="true">
    <path d="M0 372 C 280 240, 560 175, 860 148 L860 491 L0 491 Z" fill="var(--navy)"/>
    <path d="M0 362 C 280 230, 560 165, 860 138" fill="none" stroke="var(--red)" stroke-width="6"/>
  </svg>

  <div class="brand">
    <span class="brand__dot"></span>
    <span class="brand__name">Larkfield<br>Animal Blood Bank</span>
  </div>

  <div class="person">
    <p class="person__name">FULL NAME</p>
    <p class="person__title">TITLE</p>
  </div>

  <ul class="contact">
    <li class="contact__item">
      <svg class="contact__icon" viewBox="0 0 24 24"><path fill="var(--red)" d="M6.6 10.8a15.1 15.1 0 0 0 6.6 6.6l2.2-2.2c.3-.3.7-.4 1-.2 1.1.4 2.3.6 3.6.6.6 0 1 .4 1 1V20c0 .6-.4 1-1 1A17 17 0 0 1 3 4c0-.6.4-1 1-1h3.5c.6 0 1 .4 1 1 0 1.3.2 2.5.6 3.6.1.3 0 .7-.2 1z"/></svg>
      (000) 000 0000
    </li>
    <li class="contact__item">
      <svg class="contact__icon" viewBox="0 0 24 24"><rect x="2" y="5" width="20" height="14" rx="1.5" fill="var(--red)"/><path d="M3 6l9 7 9-7" fill="none" stroke="var(--navy)" stroke-width="1.8"/></svg>
      hello@larkfieldabb.org
    </li>
    <li class="contact__item">
      <svg class="contact__icon" viewBox="0 0 24 24" fill="none" stroke="var(--red)" stroke-width="1.8"><circle cx="12" cy="12" r="9.5"/><ellipse cx="12" cy="12" rx="4" ry="9.5"/><path d="M2.5 12h19M4 7h16M4 17h16"/></svg>
      www.larkfieldabb.org
    </li>
  </ul>
</section>

<section class="card card--back" aria-label="Business card back">
  <div class="brand">
    <span class="brand__dot"></span>
    <span class="brand__name">Larkfield<br>Animal Blood Bank</span>
  </div>
</section>

</body>
</html>
```